Honey packaging lable for small honey producer

We are small scale bee keepers and need a design for labels for our honey.
We curently sell honey in 2 different package sizes, 500gm and 1kg so the label would need to be suitable for both.
The plan is to print the label on brown or "craft" paper with a laser printer to give a rustic feel so the design will need to be monotone.
As we are in Australia all measurements will need to be metric
Label dimensions should be 105mm wide by 59.4mm high (so we can fit 10 labels per sheet of a4 paper).
The batch number, nett weight and number of servings per package on the nutritional label need to be able to be changed to suit the packaging size.
Designs need to be able to be opened and printed from open source software such as Open Office, Gimp or similar. If proprietary software is used there must be at least a free program to allow printing and basic manipulation of the design.
Updates

Thank you everyone for the designs you submitted. I have been surprised by the quality of work supplied and wish I had the budget to make a payment to everyone, but unfortunately that is not the case :( 

This is my first time doing anything like this and it has been an interesting experience. I have definitely learned lots and hopefully I will be a better and more concise brief writer next time :)

The only other feedback I would like to give is to read the brief carefully. There were some designers that submited color designs which weren't suitable for my needs which may have been avoided.

Thank you again for all your hard work.

All the best.

Derek & Marion.

Industry/Entity Type

Printer

Requirements
Must have
• Ferncliff Grove
honey
Nett Weight
Batch Number:
Produced by: Derek and Marion Holtby, Harlows Ridge, Victoria. 0492 317064

Nutritional panel similar to : http://www.vexolina.net.au/images/products/jars-pails-L030.jpg
Nice to have
• Produced in the Brimtons
Pure, Natural, raw.
Contains traces of pollen and wax
Honey is a natural product and may crystallize. It may be eaten as is or re-liquefied by placing the container in hot water.
Should not have
• No twee cartoon bees or skep bee hives please!

```html
<!DOCTYPE html>
<html lang="en">
<head>
<meta charset="utf-8">
<title>Ferncliff Grove Honey Labels</title>
<link rel="stylesheet" href="https://fonts.googleapis.com/css2?family=Rye&family=Roboto+Condensed:wght@400;700&family=Crimson+Pro:wght@400;700&display=swap">
<style>
  :root {
    --backdrop-start: #eb9a36;
    --backdrop-end: #d96a2e;
    --kraft: #b59f85;
    --kraft-dark: #a8917a;
    --paper: #ffffff;
    --ink: #1b1714;
  }
  * { margin: 0; padding: 0; box-sizing: border-box; }
  html, body { width: 1200px; height: 1000px; overflow: hidden; }
  body {
    position: relative;
    background: linear-gradient(100deg, var(--backdrop-start), var(--backdrop-end));
    color: var(--ink);
    font-family: "Roboto Condensed", "Arial Narrow", sans-serif;
  }
  .label {
    position: absolute;
    width: 773px;
    height: 437px;
  }
  .label--kraft { left: 232px; top: 57px; background: radial-gradient(circle at 40% 40%, var(--kraft), var(--kraft-dark)); }
  .label--white { left: 228px; top: 513px; background: var(--paper); }
  .label__frame { position: absolute; inset: 0; }
  .abs { position: absolute; }
  .center { transform: translateX(-50%); text-align: center; white-space: nowrap; }
  .display { font-family: "Rye", serif; }
  .origin { left: 148px; top: 30px; font-size: 18px; }
  .nutrition-title { left: 148px; top: 54px; font-size: 13.5px; font-weight: 700; line-height: 18px; }
  .nutrition {
    left: 24px; top: 108px;
    font-size: 14px; line-height: 18.4px;
    border-collapse: collapse;
  }
  .nutrition th { font-weight: 700; text-align: left; vertical-align: bottom; padding-bottom: 4px; line-height: 18px; }
  .nutrition td { padding: 0; }
  .nutrition td:first-child { width: 106px; font-weight: 700; }
  .nutrition td:nth-child(2) { width: 92px; }
  .nutrition .sub { padding-left: 10px; }
  .nutrition .sub2 { padding-left: 20px; }
  .footnote { left: 24px; top: 285px; font-size: 14px; line-height: 18px; }
  .footnote strong { font-weight: 700; }
  .farm-small { left: 148px; top: 336px; font-size: 19px; }
  .producer { left: 150px; top: 374px; font-size: 14.5px; font-weight: 700; line-height: 18px; }
  .farm-title { left: 533px; top: 53px; font-size: 29px; }
  .ornament { top: 55px; width: 36px; height: 30px; background: var(--ink); border-radius: 40%; opacity: .85; }
  .ornament--left { left: 333px; }
  .ornament--right { left: 692px; }
  .product-box { left: 331px; top: 117px; width: 406px; height: 112px; }
  .product-name { left: 533px; top: 126px; font-size: 84px; line-height: 96px; letter-spacing: 2px; }
  .weight { left: 533px; top: 244px; font-family: "Crimson Pro", serif; font-size: 23px; }
  .weight b { font-weight: 700; }
  .batch { left: 321px; top: 274px; font-family: "Crimson Pro", serif; font-size: 23px; }
  .batch-line { left: 508px; top: 296px; width: 232px; border-top: 2px dashed var(--ink); }
  .blurb { left: 533px; top: 320px; width: 420px; font-size: 15.5px; line-height: 19px; white-space: normal; }
  .blurb strong { font-weight: 700; }
</style>
</head>
<body>

<article class="label label--kraft">
  <svg class="label__frame" width="773" height="437" aria-hidden="true">
    <rect x="9" y="9" width="755" height="419" rx="4" fill="none" stroke="#1b1714" stroke-width="6" stroke-dasharray="7 7" stroke-linecap="round"/>
  </svg>
  <p class="abs center display origin">Product of Australia</p>
  <p class="abs center nutrition-title">Nutritional Information 500g<br>Servings per pack 33, Serving size 15g</p>
  <table class="abs nutrition">
    <tr><th></th><th>Quantity<br>Per serving</th><th>Quantity<br>Per 100g</th></tr>
    <tr><td>Energy</td><td>214kJ</td><td>1416kJ</td></tr>
    <tr><td>Protein</td><td>0.05g</td><td>0.03g</td></tr>
    <tr><td>Fat Total</td><td>0g</td><td>0g</td></tr>
    <tr><td class="sub">- Saturated</td><td>0g</td><td>0g</td></tr>
    <tr><td>Carbohydrates</td><td>12.5g</td><td>83.1g</td></tr>
    <tr><td class="sub2">-sugars*</td><td>12.5g</td><td>82.5g</td></tr>
    <tr><td>Sodium</td><td>2.3mg</td><td>15mg</td></tr>
  </table>
  <p class="abs footnote">* sugars naturally occurring in honey<br><strong>Ingredients: Pure 100% Australian Honey</strong></p>
  <p class="abs center display farm-small">Ferncliff Grove</p>
  <p class="abs center producer">Produced by: Derek &amp; Marion Holtby,<br>Harlows Ridge, Victoria. 0492 317064</p>

  <div class="abs ornament ornament--left" role="img" aria-label="Decorative flourish"></div>
  <p class="abs center display farm-title">Ferncliff Grove</p>
  <div class="abs ornament ornament--right" role="img" aria-label="Decorative flourish"></div>
  <svg class="abs product-box" width="406" height="112" aria-hidden="true">
    <rect x="3" y="3" width="400" height="106" rx="3" fill="none" stroke="#1b1714" stroke-width="6" stroke-dasharray="7 7" stroke-linecap="round"/>
  </svg>
  <p class="abs center display product-name">HONEY</p>
  <p class="abs center weight">Nett Weight: <b>500g</b></p>
  <p class="abs batch">Batch Number:</p>
  <div class="abs batch-line"></div>
  <p class="abs center blurb"><strong>Natural, pure, raw, not heat treated.</strong> Produced in the Brimtons. Contains traces of pollen and wax. Honey is a natural product and may crystallize. It may be eaten as is or re-liquefied by placing the container in hot water.</p>
</article>

<article class="label label--white">
  <svg class="label__frame" width="773" height="437" aria-hidden="true">
    <rect x="9" y="9" width="755" height="419" rx="4" fill="none" stroke="#1b1714" stroke-width="6" stroke-dasharray="7 7" stroke-linecap="round"/>
  </svg>
  <p class="abs center display origin">Product of Australia</p>
  <p class="abs center nutrition-title">Nutritional Information 500g<br>Servings per pack 33, Serving size 15g</p>
  <table class="abs nutrition">
    <tr><th></th><th>Quantity<br>Per serving</th><th>Quantity<br>Per 100g</th></tr>
    <tr><td>Energy</td><td>214kJ</td><td>1416kJ</td></tr>
    <tr><td>Protein</td><td>0.05g</td><td>0.03g</td></tr>
    <tr><td>Fat Total</td><td>0g</td><td>0g</td></tr>
    <tr><td class="sub">- Saturated</td><td>0g</td><td>0g</td></tr>
    <tr><td>Carbohydrates</td><td>12.5g</td><td>83.1g</td></tr>
    <tr><td class="sub2">-sugars*</td><td>12.5g</td><td>82.5g</td></tr>
    <tr><td>Sodium</td><td>2.3mg</td><td>15mg</td></tr>
  </table>
  <p class="abs footnote">* sugars naturally occurring in honey<br><strong>Ingredients: Pure 100% Australian Honey</strong></p>
  <p class="abs center display farm-small">Ferncliff Grove</p>
  <p class="abs center producer">Produced by: Derek &amp; Marion Holtby,<br>Harlows Ridge, Victoria. 0492 317064</p>

  <div class="abs ornament ornament--left" role="img" aria-label="Decorative flourish"></div>
  <p class="abs center display farm-title">Ferncliff Grove</p>
  <div class="abs ornament ornament--right" role="img" aria-label="Decorative flourish"></div>
  <svg class="abs product-box" width="406" height="112" aria-hidden="true">
    <rect x="3" y="3" width="400" height="106" rx="3" fill="none" stroke="#1b1714" stroke-width="6" stroke-dasharray="7 7" stroke-linecap="round"/>
  </svg>
  <p class="abs center display product-name">HONEY</p>
  <p class="abs center weight">Nett Weight: <b>500g</b></p>
  <p class="abs batch">Batch Number:</p>
  <div class="abs batch-line"></div>
  <p class="abs center blurb"><strong>Natural, pure, raw, not heat treated.</strong> Produced in the Brimtons. Contains traces of pollen and wax. Honey is a natural product and may crystallize. It may be eaten as is or re-liquefied by placing the container in hot water.</p>
</article>

</body>
</html>
```